Instagram ad design required

For an IT system house, we need an ad design for a job recruiting campaign on Instagram. A great engaging advertisement is required that encourages potential applicants to click on the ad. The recruiting funnel already exists, only an Instagram ad image should be designed. Follow-up orders for further campaigns as well as Facebook and LinkedIn are possible.
The design of the IT system house Varnholt serves as a design inspiration: www.varnholt.com
The customer should be perceived as a great, modern employer. The target group are young IT technicians who want to work in a cool and modern company. For example, the topic could be IT Super Hero wanted with corresponding graphic content.
Target Market(s)
IT system technician
Industry/Entity Type
Informatik
Other font styles liked:
- PT Sans
Look and feel
Each slider illustrates characteristics of the customer's brand and the style your logo design should communicate.

```html
<!DOCTYPE html>
<html lang="de">
<head>
<meta charset="utf-8">
<title>Varnholt – IT-Superheld gesucht</title>
<link rel="stylesheet" href="https://fonts.googleapis.com/css2?family=Lexend:wght@300;400;500;600;700;800&display=swap">
<style>
  :root{
    --bg:#effde6;
    --green:#279455;
    --neon:#5cf00c;
    --white:#ffffff;
    --photo-top:#6b6f73;
    --photo-mid:#3a3d40;
    --photo-low:#9a9ea3;
    --photo-base:#3c4e6a;
  }
  *{box-sizing:border-box;margin:0;padding:0}
  html,body{width:1200px;height:1200px;overflow:hidden;background:var(--bg)}
  .ad{position:relative;width:1200px;height:1200px;background:var(--bg);font-family:"Lexend",sans-serif;color:var(--green);overflow:hidden}
  .graphics{position:absolute;inset:0}
  .brand{position:absolute;left:62px;top:86px;display:flex;align-items:center;gap:12px;font-weight:700;font-size:30px;color:var(--green);letter-spacing:.5px;line-height:1}
  .brand-square{width:20px;height:20px;background:var(--green)}
  .kicker{position:absolute;left:464px;top:62px;font-size:63px;font-weight:600;color:var(--green);letter-spacing:-1px;line-height:1}
  .headline{position:absolute;left:326px;top:100px;font-size:186px;font-weight:700;color:var(--neon);letter-spacing:-6px;line-height:1}
  .invite{position:absolute;left:567px;top:268px;font-size:35px;font-weight:700;color:var(--green);line-height:1.28;letter-spacing:-.6px}
  .req-title{position:absolute;left:668px;top:450px;font-size:38px;font-weight:300;color:var(--green)}
  .req-list{position:absolute;left:664px;top:543px;list-style:none}
  .req-item{display:flex;align-items:center;height:88px;font-size:31px;font-weight:400;color:var(--green)}
  .req-item svg{margin-right:14px;flex:none}
  .apply-info{position:absolute;left:121px;top:1098px;color:var(--white);font-size:21px;line-height:1.5}
  .apply-info strong{font-weight:600}
  .apply-cta{position:absolute;left:776px;top:1094px;color:var(--white);font-size:41px;font-weight:700;letter-spacing:-.8px}
</style>
</head>
<body>
<main class="ad">
  <svg class="graphics" width="1200" height="1200" viewBox="0 0 1200 1200">
    <defs>
      <linearGradient id="photoTone" x1="0" y1="0" x2="0" y2="1">
        <stop offset="0" stop-color="var(--photo-top)"/>
        <stop offset=".35" stop-color="var(--photo-mid)"/>
        <stop offset=".75" stop-color="var(--photo-low)"/>
        <stop offset="1" stop-color="var(--photo-base)"/>
      </linearGradient>
    </defs>
    <g class="orbit" fill="none" stroke="var(--neon)" stroke-width="5" stroke-linecap="round">
      <path d="M69 552 A 290 290 0 0 1 561 561"/>
      <path d="M589 653 A 290 290 0 0 1 531 870"/>
      <path d="M41 712 A 290 290 0 0 0 109 883"/>
    </g>
    <g fill="var(--neon)">
      <circle cx="69" cy="552" r="13"/>
      <circle cx="589" cy="653" r="13"/>
      <circle cx="109" cy="883" r="13"/>
    </g>
    <circle class="halo" cx="314" cy="694" r="239" fill="var(--green)"/>
    <rect role="img" aria-label="Foto: lächelnder IT-Techniker im dunklen Hemd, der ein offenes PC-Gehäuse trägt"
      x="105" y="300" width="440" height="900" rx="28" fill="url(#photoTone)"/>
    <path class="band" d="M72 1075 H1161 L1139 1172 H50 Z" fill="var(--green)"/>
    <g class="chevrons" fill="none" stroke="var(--green)" stroke-width="8" stroke-linejoin="miter">
      <path d="M996 280 L1016 300 L996 320"/>
      <path d="M1016 280 L1036 300 L1016 320"/>
    </g>
  </svg>

  <div class="brand"><span class="brand-square"></span>VARNHOLT</div>
  <p class="kicker">IT-Superheld</p>
  <h1 class="headline">Gesucht</h1>
  <p class="invite">Werden Sie Teil unseres<br>großartigen Teams</p>

  <h2 class="req-title">Anforderungen:</h2>
  <ul class="req-list">
    <li class="req-item"><svg width="64" height="54" viewBox="0 0 64 54"><path d="M10 0 H64 L54 54 H0 Z" fill="var(--green)"/><path d="M32 16 V38 M21 27 H43" stroke="#fff" stroke-width="5"/></svg>Computerfähigkeiten</li>
    <li class="req-item"><svg width="64" height="54" viewBox="0 0 64 54"><path d="M10 0 H64 L54 54 H0 Z" fill="var(--green)"/><path d="M32 16 V38 M21 27 H43" stroke="#fff" stroke-width="5"/></svg>Technischer Support</li>
    <li class="req-item"><svg width="64" height="54" viewBox="0 0 64 54"><path d="M10 0 H64 L54 54 H0 Z" fill="var(--green)"/><path d="M32 16 V38 M21 27 H43" stroke="#fff" stroke-width="5"/></svg>Computer Reparaturen</li>
    <li class="req-item"><svg width="64" height="54" viewBox="0 0 64 54"><path d="M10 0 H64 L54 54 H0 Z" fill="var(--green)"/><path d="M32 16 V38 M21 27 H43" stroke="#fff" stroke-width="5"/></svg>Softwarekenntnisse</li>
  </ul>

  <p class="apply-info"><strong>Lebenslauf Senden An:</strong><br>deine E-Mail@varnholt.com</p>
  <p class="apply-cta">Jetzt bewerben!</p>
</main>
</body>
</html>
```